Neue Marke für Herrenaccessoires benötigt Flyer-Design
Zielgruppe
Wir sind ein junges Unternehmen die eine neue Marke für Herrenaccessoires aufbaut. KORVALO ist unsere neue Marke für hochwertige, stylishe Herrenaccessoires. Entstanden ist die Idee bie der Suche nach dem kompletten Look für den modernen Gentleman. Warum darf es bei den Herrenaccessoires nicht etwas mutiger zugehen in Sachen Farben und Mustern und das mit dem Anspruch hoher Materialqualität und Verarbeitung? Wo findet man komplette Accessoires-Angebote, bei denen man Krawatten, Einstecktücher, Socken, Gürtel und sogar Taschen in einem Shop farblich aufeinander abgestimmt finden kann? Diese Fragen haben wir uns gestellt und geben mit KORVALO unsere Antwort darauf. Mit KORVALO finden unsere Kunden sowohl für ihren Business- als auch für ihren Freizeitlook in Farbe und Styles perfekt kombinierbare Accessoires, die wir in von uns persönlich ausgewählten Manufakturen in Italien und der Türkei mit Sorgfalt und Know-how fertigen lassen.
Vom kontrastreichen, mutigen trendy Muster- und Farbmix zur klassischen Kombination Ton in Ton mit aktuellen Farben.
Unsere Zielgruppen sind mode- und stilbewusste Herren im Alter von 30 - 50.
Aufgabenstellung
Das Design sollte sich an unserem Web-Shop www.korvalo-shop.example orientieren.
Die Market KORVALO clean, minimalistisch und edel wahrgenommen werden.
Wir möchten die erste Marketingkampage mit einem Flyer starten. Die Flyer werden über eine Textilreinigungsfirma an die Reinigungsbügel (bei Hemden) befestigt. Aus diesem Grund sollte das Layout die Maße von ca. Breite: 9,5 cm x Höhe: 20 cm orientieren. Damit der Flyer (2seitig) auch an die Bügel umgehängt werden kann, muss oben auf dem Flyer ein Loch mit einem Durchmesser von 3 cm ein berücksichtigt werden.

```html
<!DOCTYPE html>
<html lang="de">
<head>
<meta charset="utf-8">
<title>KORVALO Bügelflyer</title>
<link rel="stylesheet" href="https://fonts.googleapis.com/css2?family=Lato:wght@400;700;900&display=swap">
<style>
  :root {
    --stage: #d6d6d6;
    --paper: #ffffff;
    --ink: #111111;
    --pink: #e45ea9;
    --blue: #1d3f9c;
    --hole: #b9b9b9;
    --photo-light: #f2f2f2;
    --photo-mid: #a9a9a9;
    --photo-dark: #3c3c3c;
  }
  * { box-sizing: border-box; margin: 0; padding: 0; }
  html, body { width: 1200px; height: 857px; overflow: hidden; }
  body {
    background: var(--stage);
    font-family: "Lato", Arial, sans-serif;
    color: var(--ink);
    position: relative;
  }
  .flyer {
    position: absolute;
    top: 63px;
    width: 255px;
    height: 729px;
    background: var(--paper);
    overflow: hidden;
  }
  .flyer--front { left: 199px; }
  .flyer--back { left: 648px; }
  .hanger-hole {
    position: absolute;
    top: 21px;
    left: 50%;
    margin-left: -53px;
    width: 106px;
    height: 106px;
    border-radius: 50%;
    background: radial-gradient(circle at 50% 40%, #c4c4c4, var(--hole));
    z-index: 3;
  }
  .front-photo {
    position: absolute;
    inset: 0;
    background:
      radial-gradient(ellipse at 20% 55%, var(--photo-dark) 0%, rgba(60,60,60,0.6) 30%, transparent 60%),
      linear-gradient(90deg, var(--photo-mid) 0%, var(--photo-light) 70%, #fafafa 100%);
  }
  .front-band {
    position: absolute;
    left: 0;
    top: 619px;
    width: 100%;
    height: 65px;
    background: rgba(255,255,255,0.95);
    display: flex;
    align-items: center;
    z-index: 2;
  }
  .brand-mark {
    margin-left: 19px;
    width: 56px;
    display: flex;
    flex-direction: column;
    align-items: flex-start;
  }
  .brand-mark__name {
    font-size: 8px;
    font-weight: 700;
    letter-spacing: 0.5px;
    color: var(--ink);
    line-height: 1;
    margin-bottom: 2px;
  }
  .brand-mark__square {
    width: 40px;
    height: 40px;
    background: var(--ink);
  }
  .front-headline {
    margin-left: 18px;
    color: var(--pink);
    font-weight: 900;
    font-size: 19px;
    line-height: 1.05;
    letter-spacing: 0.3px;
    text-transform: uppercase;
  }
  .front-footer {
    position: absolute;
    top: 692px;
    left: 19px;
    font-size: 10px;
    color: #ffffff;
    z-index: 2;
  }
  .front-footer .url { color: var(--pink); }

  .back-copy {
    position: absolute;
    top: 486px;
    width: 100%;
    text-align: center;
  }
  .back-copy__lead {
    font-size: 14px;
    font-weight: 700;
  }
  .back-copy__lead .url { color: var(--blue); }
  .back-copy__body {
    margin-top: 14px;
    font-size: 9.5px;
    line-height: 1.35;
  }
  .back-copy__body + .back-copy__body { margin-top: 8px; }

  .voucher-band {
    position: absolute;
    top: 615px;
    left: 0;
    width: 100%;
    height: 75px;
    background: var(--ink);
    display: flex;
  }
  .voucher-band__brand {
    width: 66px;
    height: 100%;
    background: var(--paper);
    display: flex;
    flex-direction: column;
    align-items: center;
    justify-content: center;
    border: 1px solid var(--ink);
  }
  .voucher-band__brand .brand-mark__square { width: 42px; height: 42px; }
  .voucher-band__brand .brand-mark__name { margin-bottom: 3px; }
  .voucher {
    padding: 18px 0 0 12px;
    color: #ffffff;
  }
  .voucher__code {
    font-size: 13px;
    font-weight: 700;
  }
  .voucher__terms {
    margin-top: 5px;
    font-size: 7px;
    line-height: 1.3;
    color: #dddddd;
  }
</style>
</head>
<body>

  <section class="flyer flyer--front" aria-label="Vorderseite">
    <div class="front-photo" role="img" aria-label="Schwarzweiß-Foto eines Herrn im Anzug mit pinker Krawatte und Einstecktuch am Fenster"></div>
    <div class="hanger-hole"></div>
    <div class="front-band">
      <div class="brand-mark">
        <span class="brand-mark__name">KORVALO</span>
        <span class="brand-mark__square"></span>
      </div>
      <p class="front-headline">Lust auf einen<br>neuen Style?</p>
    </div>
    <p class="front-footer">Lass Dich inspirieren: <span class="url">www.korvalo-shop.example</span></p>
  </section>

  <section class="flyer flyer--back" aria-label="Rückseite">
    <div class="hanger-hole"></div>
    <div class="back-copy">
      <p class="back-copy__lead">Lass Dich inspirieren: <span class="url">www.korvalo-shop.example</span></p>
      <p class="back-copy__body">Der neue Online-Shop mit hochwertigen,<br>stylishen Herrenaccessoires für den modernen Gentleman.</p>
      <p class="back-copy__body">Oder besuch uns hier:<br>Instagram: korvalo-official<br>Facebook: KORVALO</p>
    </div>
    <div class="voucher-band">
      <div class="voucher-band__brand">
        <span class="brand-mark__name">KORVALO</span>
        <span class="brand-mark__square"></span>
      </div>
      <div class="voucher">
        <p class="voucher__code">Ihr 20% Rabattcode*: Kleenxxx</p>
        <p class="voucher__terms">*Gültig bis zum 00/00/0000<br>Nicht kombinierbar mit anderen Rabattaktionen</p>
      </div>
    </div>
  </section>

</body>
</html>
```